Just Listed and Just Sold Post Cards. I have attached copies of what I have had in the past for reference. I have a new company logo attached that needs to be used. Please also include website: www.marshwillowfinder.com
email. brendakowal@brendakowalrealty.com
phone 555-203-7748
Target Market(s)
home and land owners
Font styles to use
Sans Serif
Colors
0356a4
Requirements
Must have
- I need a South Gulf Cove Just Listed Card and a Just Sold Card
- Must have My name company name logo website email phone number
- back should read _______. on your block of South Gulf Cove has just SOLD at $________ on _____________________ similar to the one I have attached.
Nice to have
- I like how the attached postcards from before have the shaded picture on the back of the picture on the front. I like to have the aerial as one main photo and the photo with the boat as the other main photo.
- Integrate my Brenda Kowal logo with the KT Vista logo

```html
<!DOCTYPE html>
<html lang="en">
<head>
<meta charset="utf-8">
<title>Just Sold Postcard – South Gulf Cove</title>
<link href="https://fonts.googleapis.com/css2?family=Oswald:wght@600&family=Raleway:wght@300;400;600&display=swap" rel="stylesheet">
<style>
  :root {
    --brand-blue: #0356a4;
    --sky: #7fb2ea;
    --lavender: #c9c2f2;
    --palm: #3f7a3a;
    --water: #1f4f8a;
    --blush: #e9d6dc;
    --panel-blue: rgba(70, 140, 200, 0.8);
    --white: #ffffff;
    --ink: #1d1d2b;
    --accent-orange: #e36b1c;
    --brokerage-grey: #5a6a86;
    --stage: #161616;
  }
  * { box-sizing: border-box; margin: 0; padding: 0; }
  html, body { width: 1200px; height: 1200px; overflow: hidden; }
  body {
    background: var(--stage);
    font-family: "Raleway", sans-serif;
    position: relative;
  }

  /* ---------- Front ---------- */
  .card-front {
    position: absolute; left: 50px; top: 50px;
    width: 760px; height: 550px; overflow: hidden;
    box-shadow: 0 10px 30px rgba(0,0,0,.6);
  }
  .front-photo {
    position: absolute; inset: 0;
    background: linear-gradient(180deg,
      var(--sky) 0%, #a9cdf4 38%, var(--palm) 46%, #5b8c4f 55%,
      var(--water) 64%, #163c6e 100%);
  }
  .front-tint-top {
    position: absolute; inset: 0;
    background: linear-gradient(135deg, rgba(201,194,242,.15), rgba(201,194,242,.85));
    clip-path: polygon(12% 0, 100% 0, 100% 8%, 62% 52%);
  }
  .front-tint-right {
    position: absolute; inset: 0;
    background: rgba(180,175,240,.55);
    clip-path: polygon(48% 0, 100% 0, 100% 58%);
  }
  .front-wedge-center {
    position: absolute; inset: 0;
    background: rgba(110,160,230,.35);
    clip-path: polygon(22% 38%, 40% 25%, 62% 52%);
  }
  .front-wedge-low {
    position: absolute; inset: 0;
    background: rgba(60,120,210,.45);
    clip-path: polygon(46% 100%, 87% 63%, 100% 72%, 100% 100%);
  }
  .front-corner {
    position: absolute; inset: 0;
    background: linear-gradient(0deg, rgba(255,255,255,.9), rgba(233,214,220,.8));
    clip-path: polygon(0 73%, 18% 73%, 46% 100%, 0 100%);
  }
  .headline {
    position: absolute; right: 38px; top: 26px;
    font-family: "Oswald", sans-serif; font-weight: 600;
    font-size: 118px; line-height: 1; letter-spacing: -2px;
    color: var(--white); text-shadow: 0 3px 8px rgba(40,40,90,.35);
  }
  .subhead {
    position: absolute; right: 44px; top: 148px;
    font-weight: 300; font-size: 34px; letter-spacing: 1px; color: var(--white);
  }
  .agent-mark {
    position: absolute; right: 40px; top: 204px; text-align: right;
  }
  .agent-name {
    display: flex; align-items: center; gap: 8px; justify-content: flex-end;
    font-weight: 600; font-size: 21px; letter-spacing: 1.5px; color: var(--ink);
  }
  .agent-name .dot { width: 14px; height: 14px; border-radius: 50%; background: var(--ink); }
  .agent-title { font-size: 10px; font-weight: 600; letter-spacing: 1.5px; color: var(--ink); margin-top: 2px; }
  .brokerage-front {
    position: absolute; left: 52px; bottom: 36px;
  }
  .brokerage-name {
    display: flex; align-items: center; gap: 8px;
    font-weight: 600; font-size: 26px; letter-spacing: 2px; color: var(--brokerage-grey);
  }
  .brokerage-name .square { width: 14px; height: 14px; background: var(--brokerage-grey); }
  .brokerage-sub { font-size: 9px; letter-spacing: 2px; color: #6f7b90; margin-top: 3px; padding-left: 22px; }

  /* ---------- Back ---------- */
  .card-back {
    position: absolute; left: 390px; top: 625px;
    width: 760px; height: 530px; overflow: hidden;
    box-shadow: 0 10px 30px rgba(0,0,0,.6);
  }
  .back-photo {
    position: absolute; inset: 0;
    background: linear-gradient(180deg,
      #3f86d2 0%, #7fb1e2 30%, #8fb6d8 40%, #a9bfcf 55%, #cfd8de 78%, #ffffff 100%);
  }
  .stamp-box {
    position: absolute; right: 76px; top: 28px; width: 150px; height: 160px;
    border: 1px dashed rgba(255,255,255,.9);
  }
  .logo-panel {
    position: absolute; left: 26px; top: 52px; width: 260px; height: 140px;
    background: rgba(255,255,255,.85); border-radius: 4px;
    padding: 20px 18px;
  }
  .logo-panel .agent-name { justify-content: flex-start; color: var(--brand-blue); font-size: 20px; }
  .logo-panel .agent-name .dot { background: var(--brand-blue); }
  .logo-panel .agent-title { color: var(--accent-orange); padding-left: 22px; }
  .logo-panel .brokerage-name { font-size: 18px; margin-top: 20px; }
  .logo-panel .brokerage-sub { font-size: 7px; }
  .message-panel {
    position: absolute; left: 44px; top: 218px; width: 330px;
    background: var(--panel-blue); border-radius: 3px;
    padding: 12px 14px 14px; color: var(--white); font-size: 13px; line-height: 1.3;
  }
  .blank { background: rgba(255,255,255,.85); border-radius: 2px; display: inline-block; height: 26px; }
  .blank-street { width: 100%; display: block; }
  .message-line { margin-top: 10px; }
  .price-row { display: flex; align-items: center; gap: 6px; margin-top: 10px; }
  .blank-price { width: 110px; }
  .blank-date { width: 110px; }
  .contact-list { list-style: none; margin-top: 18px; font-size: 13px; line-height: 1.25; }
  .contact-list li { display: flex; align-items: center; gap: 8px; margin-top: 5px; white-space: nowrap; }
  .contact-list svg { width: 14px; height: 14px; fill: var(--white); flex: none; }
</style>
</head>
<body>

<section class="card-front" aria-label="Postcard front">
  <div class="front-photo" role="img" aria-label="Canal-side homes with palm trees and a fishing boat, blended with an aerial view of the canals"></div>
  <div class="front-tint-top"></div>
  <div class="front-tint-right"></div>
  <div class="front-wedge-center"></div>
  <div class="front-wedge-low"></div>
  <div class="front-corner"></div>

  <h1 class="headline">JUST SOLD</h1>
  <p class="subhead">South Gulf Cove</p>

  <div class="agent-mark">
    <div class="agent-name"><span class="dot"></span>BRENDA KOWAL</div>
    <div class="agent-title">BROKER ASSOCIATE</div>
  </div>

  <div class="brokerage-front">
    <div class="brokerage-name"><span class="square"></span>KT VISTA</div>
    <div class="brokerage-sub">KESTREL-THORNE REALTY</div>
  </div>
</section>

<section class="card-back" aria-label="Postcard back">
  <div class="back-photo" role="img" aria-label="Aerial view of the coastline and canal neighbourhood, fading to white"></div>
  <div class="stamp-box" aria-label="Stamp area"></div>

  <div class="logo-panel">
    <div class="agent-name"><span class="dot"></span>BRENDA KOWAL</div>
    <div class="agent-title">BROKER ASSOCIATE</div>
    <div class="brokerage-name"><span class="square"></span>KT VISTA</div>
    <div class="brokerage-sub">KESTREL-THORNE REALTY</div>
  </div>

  <div class="message-panel">
    <span class="blank blank-street"></span>
    <p class="message-line">on Your block os South Gulf Cove<br>has just LISTED</p>
    <div class="price-row">at $ <span class="blank blank-price"></span> on <span class="blank blank-date"></span></div>
    <p class="message-line">Please, contact me if You are interested in buying or selling the property in this area</p>
    <ul class="contact-list">
      <li><svg viewBox="0 0 16 16"><circle cx="8" cy="8" r="7"/></svg>www.marshwillowfinder.com</li>
      <li><svg viewBox="0 0 16 16"><path d="M1 3h14v10H1z M1 3l7 6 7-6" stroke="#468cc8" stroke-width="1.2"/></svg>brendakowal@brendakowalrealty.com</li>
      <li><svg viewBox="0 0 16 16"><path d="M3 1l3 3-2 2c1 2 3 4 6 6l2-2 3 3-2 2C7 15 1 9 1 3z"/></svg>phone 555-203-7748</li>
      <li><svg viewBox="0 0 16 16"><path d="M8 1l7 7h-2v7H10v-4H6v4H3V8H1z"/></svg>PO BOX 418, CEDAR HAVEN, FL 30417</li>
    </ul>
  </div>
</section>

</body>
</html>
```